Poster design for - Glowing Meadow Festival

To design a dynamic illustrated Glowing Meadow Festival poster.
The dates are: 9-11 July 2020
Location: Tarlow Campsite, Fernhollow, Greenshire
www.glowingmeadow.co.uk

Here is some text about the event to give you an idea. You can take elements from it if you like:

A Gathering of Female Energy to Ignite and Embrace the Power of Woman with Mother Earth.

Target Market(s)

Women festival goers.

Industry/Entity Type

Festival

Colors

Designer to choose colors to be used in the design.

Requirements
Must have
• Glowing Meadow Logo - but this can be altered to look washed out.
• Date, location, website url.
Nice to have
• Earthy, hippy, festival look.

```html
<!DOCTYPE html>
<html lang="en">
<head>
<meta charset="utf-8">
<title>Glowing Meadow Festival – Poster</title>
<link href="https://fonts.googleapis.com/css2?family=Barlow+Condensed:ital,wght@0,700;1,600;1,800;1,900&display=swap" rel="stylesheet">
<style>
  :root {
    --page: #f2f2f2;
    --magenta: #e8117f;
    --cyan: #1fb3e8;
    --yellow: #f6ec25;
    --orange: #ef7a1e;
    --flame: #e8562a;
    --purple: #5f2e8e;
    --white: #ffffff;
  }
  html, body {
    margin: 0;
    padding: 0;
    width: 845px;
    height: 1200px;
    overflow: hidden;
    background: var(--page);
  }
  .poster {
    position: absolute;
    left: 131px;
    top: 186px;
    width: 602px;
    height: 854px;
    overflow: hidden;
    font-family: "Barlow Condensed", "Arial Narrow", sans-serif;
  }
  .paint-wash {
    position: absolute;
    inset: 0;
    background:
      radial-gradient(ellipse 220px 300px at 0% 80%, var(--cyan) 0%, rgba(31,179,232,0.6) 45%, rgba(31,179,232,0) 100%),
      radial-gradient(ellipse 200px 320px at 2% 30%, var(--magenta) 0%, rgba(232,17,127,0.75) 50%, rgba(232,17,127,0) 100%),
      radial-gradient(ellipse 210px 140px at 78% 0%, var(--orange) 0%, rgba(239,122,30,0.5) 55%, rgba(239,122,30,0) 100%),
      linear-gradient(90deg, var(--white) 0%, var(--white) 52%, var(--yellow) 64%, var(--yellow) 100%);
  }
  .brand {
    position: absolute;
    left: 0;
    right: 0;
    top: 212px;
    display: flex;
    align-items: center;
    justify-content: center;
    gap: 10px;
  }
  .brand-dot {
    width: 22px;
    height: 22px;
    border-radius: 50%;
    background: var(--flame);
  }
  .brand-name {
    font-weight: 700;
    font-size: 50px;
    letter-spacing: 2px;
    text-transform: uppercase;
    color: var(--flame);
    line-height: 1;
  }
  .accent-shape {
    position: absolute;
    left: 0;
    top: 0;
  }
  .headline {
    position: absolute;
    left: 102px;
    top: 318px;
    margin: 0;
    font-style: italic;
    font-weight: 900;
    font-size: 148px;
    line-height: 0.74;
    letter-spacing: -2px;
    color: var(--purple);
    text-transform: uppercase;
    white-space: nowrap;
    transform: scaleX(0.82);
    transform-origin: left top;
  }
  .tagline {
    position: absolute;
    left: 102px;
    top: 558px;
    margin: 0;
    font-style: italic;
    font-weight: 800;
    font-size: 35px;
    line-height: 0.98;
    color: var(--purple);
    text-transform: uppercase;
    white-space: nowrap;
  }
  .details {
    position: absolute;
    top: 650px;
    left: 104px;
    display: flex;
    gap: 22px;
    font-style: italic;
    font-weight: 600;
    font-size: 15px;
    line-height: 1.2;
    color: var(--magenta);
  }
  .detail {
    display: flex;
    align-items: flex-start;
    gap: 4px;
  }
  .detail svg { flex: none; margin-top: 1px; }
  .website {
    position: absolute;
    left: 0;
    right: 0;
    top: 796px;
    text-align: center;
    font-weight: 700;
    font-size: 15px;
    letter-spacing: 9.5px;
    color: var(--purple);
    text-transform: uppercase;
  }
</style>
</head>
<body>
  <main class="poster">
    <div class="paint-wash" role="img" aria-label="Textured paint splashes in magenta, cyan, orange and yellow"></div>

    <div class="brand">
      <span class="brand-dot"></span>
      <span class="brand-name">Glowing Meadow</span>
    </div>

    <svg class="accent-shape" width="602" height="854" viewBox="0 0 602 854" aria-hidden="true">
      <polygon points="429,560 486,560 486,682 364,682" fill="var(--magenta)"/>
    </svg>

    <h1 class="headline">Ignite&amp;<br>Embrace</h1>

    <p class="tagline">The power of woman<br>with Mother Earth</p>

    <div class="details">
      <div class="detail location">
        <svg width="12" height="16" viewBox="0 0 12 16" aria-hidden="true">
          <path d="M6 0C2.7 0 0 2.6 0 5.9 0 10.2 6 16 6 16s6-5.8 6-10.1C12 2.6 9.3 0 6 0zm0 8.3a2.4 2.4 0 1 1 0-4.8 2.4 2.4 0 0 1 0 4.8z" fill="var(--magenta)"/>
        </svg>
        <span>Tarlow Campsite, Fernhollow,<br>Greenshire</span>
      </div>
      <div class="detail date">
        <svg width="20" height="18" viewBox="0 0 20 18" aria-hidden="true">
          <rect x="1" y="3" width="18" height="14" rx="2" fill="none" stroke="var(--magenta)" stroke-width="2"/>
          <rect x="1" y="3" width="18" height="4" fill="var(--magenta)"/>
          <rect x="5" y="0" width="2" height="5" fill="var(--magenta)"/>
          <rect x="13" y="0" width="2" height="5" fill="var(--magenta)"/>
          <g fill="var(--magenta)">
            <rect x="4" y="9" width="3" height="2"/><rect x="8.5" y="9" width="3" height="2"/><rect x="13" y="9" width="3" height="2"/>
            <rect x="4" y="12.5" width="3" height="2"/><rect x="8.5" y="12.5" width="3" height="2"/><rect x="13" y="12.5" width="3" height="2"/>
          </g>
        </svg>
        <span>9-11 July<br>2020</span>
      </div>
    </div>

    <div class="website">www.glowingmeadow.co.uk</div>
  </main>
</body>
</html>
```